Business Card Design needed for start up company Pramora

In need of a new business card designed for a start up company based in Sydney, Pramora is a new start up innovative Company, our mission it to make property accessible for everyday Australian and to become the leading Real Estate platform in Australia. We want it to be fresh and clean.

Industry/Entity Type

Financial

Contact Information for Business Card

Section for Name
Section for Title

PRAMORA - Where Doors Open Wide
Mobile:
Direct:

Font styles to use
Sans Serif

Colors
33a6d7
0692cd
0255a3
ffffff

Requirements
Must have
• Logo, all business card details

```html
<!DOCTYPE html>
<html lang="en">
<head>
<meta charset="utf-8">
<title>Pramora Business Card</title>
<link rel="stylesheet" href="https://fonts.googleapis.com/css2?family=Roboto+Condensed:wght@400;700&family=Roboto:wght@400&display=swap">
<style>
  :root {
    --sky: #33a6d7;
    --ocean: #0692cd;
    --navy: #0255a3;
    --deep: #2b5a8c;
    --white: #ffffff;
    --ink: #4a4a4a;
    --backdrop: #eceef0;
    --rule: #4aaedb;
  }
  * { margin: 0; padding: 0; box-sizing: border-box; }
  html, body { width: 1200px; height: 1200px; overflow: hidden; }
  body {
    background: var(--backdrop);
    font-family: "Roboto", sans-serif;
    position: relative;
  }
  .card {
    position: absolute;
    left: 260px;
    width: 680px;
    height: 400px;
    background: var(--white);
    box-shadow: 0 6px 18px rgba(0,0,0,0.12);
    overflow: hidden;
  }
  .card--front { top: 120px; }
  .card--back { top: 660px; }

  .brand {
    position: absolute;
    top: 48px; left: 0; right: 0;
    display: flex; justify-content: center; align-items: center; gap: 14px;
  }
  .brand__dot {
    width: 74px; height: 74px; border-radius: 50%;
    background: var(--sky);
  }
  .brand__name {
    font-family: "Roboto Condensed", sans-serif;
    font-weight: 700; font-size: 62px; letter-spacing: 1px;
    color: var(--deep);
  }
  .person {
    position: absolute; top: 150px; left: 0; right: 0; text-align: center;
  }
  .person__name {
    font-family: "Roboto Condensed", sans-serif;
    font-weight: 700; font-size: 34px; color: var(--sky); letter-spacing: 0.5px;
  }
  .person__role {
    margin-top: 6px;
    font-family: "Roboto Condensed", sans-serif;
    font-size: 20px; color: var(--ink);
    display: flex; justify-content: center; align-items: center; gap: 6px;
  }
  .person__role svg { width: 18px; height: 18px; }

  .divider-h {
    position: absolute; top: 262px; left: 0; right: 0;
    height: 1px; background: var(--rule);
  }
  .divider-v {
    position: absolute; top: 262px; left: 340px;
    width: 1px; height: 108px; background: var(--rule);
  }
  .detail {
    position: absolute; top: 244px; width: 340px;
    text-align: center;
    font-size: 18px; line-height: 28px; color: var(--ink);
  }
  .detail--web { left: 0; }
  .detail--address { left: 340px; }
  .detail__icon {
    display: block; margin: 0 auto 10px;
    width: 36px; height: 36px;
  }
  .band {
    position: absolute; left: 0; right: 0; bottom: 0; height: 16px;
    background: var(--sky);
  }
  .band-line {
    position: absolute; left: 0; right: 0; bottom: 20px; height: 2px;
    background: var(--sky);
  }

  .back__mark {
    position: absolute; top: 80px; left: 275px;
    width: 130px; height: 130px; border-radius: 50%;
    background: var(--sky);
  }
  .back__name {
    position: absolute; top: 232px; left: 0; right: 0; text-align: center;
    font-family: "Roboto Condensed", sans-serif;
    font-weight: 700; font-size: 22px; color: var(--ocean); letter-spacing: 0.5px;
  }
  .back__tagline {
    position: absolute; top: 262px; left: 0; right: 0; text-align: center;
    font-family: "Roboto Condensed", sans-serif;
    font-size: 20px; color: var(--ink);
  }
</style>
</head>
<body>

<section class="card card--front">
  <div class="brand">
    <span class="brand__dot"></span>
    <span class="brand__name">PRAMORA</span>
  </div>

  <div class="person">
    <div class="person__name">LIAM CARTER</div>
    <div class="person__role">
      <span>Director |</span>
      <svg viewBox="0 0 20 20" aria-hidden="true">
        <circle cx="10" cy="10" r="10" fill="var(--navy)"/>
        <path d="M5 8.5c0-1.5 2.2-2.5 5-2.5s5 1 5 2.5v0.8h-2.4v-1.1H7.4v1.1H5z M7 10h6l1 4H6z" fill="#fff"/>
      </svg>
      <span>1-800-413275</span>
    </div>
  </div>

  <div class="divider-h"></div>
  <div class="divider-v"></div>

  <div class="detail detail--web">
    <svg class="detail__icon" viewBox="0 0 36 36" aria-hidden="true">
      <circle cx="18" cy="18" r="18" fill="var(--navy)"/>
      <g fill="none" stroke="#fff" stroke-width="1.3">
        <circle cx="18" cy="18" r="9"/>
        <ellipse cx="18" cy="18" rx="4" ry="9"/>
        <line x1="9" y1="18" x2="27" y2="18"/>
        <line x1="10.5" y1="13.5" x2="25.5" y2="13.5"/>
        <line x1="10.5" y1="22.5" x2="25.5" y2="22.5"/>
      </g>
    </svg>
    <div>www.pramora.com</div>
    <div>liam@pramora.com</div>
  </div>

  <div class="detail detail--address">
    <svg class="detail__icon" viewBox="0 0 36 36" aria-hidden="true">
      <circle cx="18" cy="18" r="18" fill="var(--navy)"/>
      <path d="M18 9l9 8h-2.5v9h-4.5v-6h-4v6h-4.5v-9H9z" fill="#fff"/>
    </svg>
    <div>Dummy city</div>
    <div>Dummy Country Land</div>
  </div>

  <div class="band-line"></div>
  <div class="band"></div>
</section>

<section class="card card--back">
  <div class="back__mark"></div>
  <div class="back__name">PRAMORA</div>
  <div class="back__tagline">where doors open wide</div>
</section>

</body>
</html>
```